Business Card Design

Harbourline Recruitment is a specialist financial services recruitment company and implementation partner

Industry/Entity Type

Business

Contact Information for Business Card

Tom Ashford
Harbourline Recruitment Ltd
e:tom.ashford@harbourline-staffing.com
m:07834 206 148
m:07712 438 560
s: tommashford

```html
<!DOCTYPE html>
<html lang="en">
<head>
<meta charset="utf-8">
<title>Tom Ashford – Harbourline Recruitment Ltd</title>
<link href="https://fonts.googleapis.com/css2?family=Cinzel:wght@400;500&family=Montserrat:wght@400;500&display=swap" rel="stylesheet">
<style>
  :root {
    --cyan: #00f5fb;
    --white: #ffffff;
    --ink: #111111;
    --strip: #161616;
  }
  * { margin: 0; padding: 0; box-sizing: border-box; }
  html, body { width: 1200px; height: 720px; overflow: hidden; background: var(--white); }
  .card {
    position: relative; width: 1200px; height: 720px; overflow: hidden;
    background: var(--white); color: var(--ink);
    font-family: "Cinzel", Georgia, serif;
  }
  .side-strip {
    position: absolute; left: 0; top: 0; width: 154px; height: 720px;
    background: var(--strip);
  }
  .icon-box {
    position: absolute; left: 109px; width: 91px; height: 91px;
    background: var(--cyan);
    display: flex; align-items: center; justify-content: center;
  }
  .icon-box--phone { top: 90px; }
  .icon-box--web { top: 221px; }
  .phones {
    position: absolute; left: 226px; top: 96px;
    font-family: "Montserrat", Arial, sans-serif; font-size: 30px; font-weight: 500;
    line-height: 45px; letter-spacing: 0.5px;
  }
  .email {
    position: absolute; left: 217px; top: 238px;
    font-size: 27px; letter-spacing: 0.3px; text-transform: uppercase; line-height: 1.2;
  }
  .skype {
    position: absolute; left: 217px; top: 278px;
    font-family: "Montserrat", Arial, sans-serif; font-size: 20px; font-weight: 500;
    letter-spacing: 0.5px;
  }
  .name-banner {
    position: absolute; left: 592px; top: 78px; width: 608px; height: 158px;
    background: var(--cyan);
    clip-path: polygon(0 0, 100% 0, 100% 100%, 87px 100%);
  }
  .person-name {
    position: absolute; left: 668px; top: 97px; width: 500px; text-align: center;
    color: var(--white); font-size: 64px; font-weight: 400; line-height: 1;
    text-transform: uppercase; letter-spacing: 1px;
  }
  .person-role {
    position: absolute; left: 668px; top: 172px; width: 500px; text-align: center;
    color: var(--white); font-size: 23px; font-weight: 500; letter-spacing: 1px;
  }
  .company {
    position: absolute; left: 185px; top: 570px;
    display: flex; align-items: center; gap: 20px;
  }
  .company-mark { width: 40px; height: 40px; background: var(--cyan); }
  .company-name {
    font-size: 50px; font-weight: 400; text-transform: uppercase;
    letter-spacing: 0.5px; line-height: 1; color: var(--ink);
  }
  .address {
    position: absolute; left: 243px; top: 636px;
    font-size: 26px; font-weight: 500; letter-spacing: 1px;
  }
</style>
</head>
<body>
<div class="card">
  <div class="side-strip"></div>

  <div class="icon-box icon-box--phone">
    <svg width="42" height="42" viewBox="0 0 24 24" aria-hidden="true">
      <path fill="#fff" d="M6.6 10.8a15.1 15.1 0 0 0 6.6 6.6l2.2-2.2c.3-.3.7-.4 1-.2 1.1.4 2.3.6 3.6.6.6 0 1 .4 1 1V20c0 .6-.4 1-1 1A17 17 0 0 1 3 4c0-.6.4-1 1-1h3.5c.6 0 1 .4 1 1 0 1.3.2 2.5.6 3.6.1.3 0 .7-.2 1z"/>
    </svg>
  </div>
  <div class="phones">
    <div>07834 206 148</div>
    <div>07712 438 560</div>
  </div>

  <div class="icon-box icon-box--web">
    <svg width="44" height="44" viewBox="0 0 24 24" aria-hidden="true">
      <circle cx="12" cy="12" r="10" fill="#fff"/>
      <path fill="var(--cyan)" d="M7 6.5c1.5-.8 3-.6 3.6.4.5.9-.4 1.8-1.3 2.2-.8.4-.5 1.6.4 1.9 1 .3 1.2 1.5.5 2.3-.9 1-2.2.4-2.7-.7-.5-1-1.4-1.4-2.2-1.6.1-2 .8-3.5 1.7-4.5zM14 13.5c1-.4 2.4 0 2.8 1 .4 1-.2 2.4-1.2 3.2-.9.7-1.9.3-1.9-.8 0-.8-.6-1.3-.4-2.1.1-.6.3-1.1.7-1.3zM15 5.5c1.2.3 2.3 1 3 2-.6.3-1.4.1-1.9-.3-.5-.4-1.1-.9-1.1-1.7z"/>
    </svg>
  </div>
  <div class="email">tom.ashford@harbourline-staffing.com</div>
  <div class="skype">s: tommashford</div>

  <div class="name-banner"></div>
  <h1 class="person-name">Tom Ashford</h1>
  <p class="person-role">Financial Recruitement Specialist</p>

  <div class="company">
    <span class="company-mark" aria-hidden="true"></span>
    <span class="company-name">Harbourline Recruitment Ltd</span>
  </div>
  <p class="address">14 Quayside Court, Mariner Way, Hertfordshire, WD6 9LR</p>
</div>
</body>
</html>
```